HomePage Design for Bright Journeys - once-in-a-lifetime experiences for busy working people

Design a homepage for the Bright Journeys (www.brightjourneys-demo.com) website compatible with further web pages and the design briefing documents attached

BJ HomePage Design Brief
We are seeking website HomePage designs incorporating our new Logo and colour scheme, for Bright Journeys (www.brightjourneys-demo.com) to go with the site functionality and wireframe ideas attached.
The website HomePage design needs to
• Incorporate and be consistent with the BJ Logo and its colour scheme attached.
• Express the brand values of being inspirational, high quality, upscale, cultured, aspirational, and contemporary – even somewhat ‘hip’. Probably positioned somewhere between Mervyn Pask (Deluxe Travel) and Velvet Harbour (Hip Travel) – see https://www.mervynpask-demo.com and https://www.velvetharbour-demo.com .
• Be instantly recognisable and different from other travel websites and instantly communicate the nature of the brand proposition and target customer base.
• Appeal to our core 25-55 affluent businesspeople demographic
• Work in the UK, US/Canada and Australia/NZ and ultimately in mainland Europe.
• Use fonts and colours that are easily reproduced online and compatible with nearly all browsers.
• Be part of a responsive website design, that can be used both on Desktops and laptops but also with tablets and mobile ‘phones (hence content not too wide across the page)
• Feature the strapline ‘Bright Journeys in less than 7 Days’
• Work with the and wireframes and processes shown in the attached presentation – although intended as a guide only these features and processes all need to be incorporated into the HomePage.
• Make full use of high quality images and video to convey our brand proposition and products

Target Market(s)

25-55 affluent businesspeople

Industry/Entity Type

Travel Industry

Number of Pages Required

1 page

Font styles to use
Sans Serif

Colors
0455a3
00a88f

Requirements
Must have
• • Incorporate and be consistent with the BJ Logo and its colour scheme attached.
• • Express the brand values of being inspirational, high quality, upscale, cultured, aspirational, and contemporary – even somewhat ‘hip’. Probably positioned somewhere between Mervyn Pask (Deluxe Travel) and Velvet Harbour (Hip Travel) – see https://www.mervynpask-demo.com and https://www.velvetharbour-demo.com .
• • Be instantly recognisable and different from other travel websites and instantly communicate the nature of the brand proposition and target customer base.
• • Appeal to our core 25-55 affluent businesspeople demographic
• • Be part of a responsive website design, that can be used both on Desktops and laptops but also with tablets and mobile ‘phones (hence content not too wide across the page)
• • Feature the strapline ‘Bright Journeys in less than 7 Days’
• • Work with the and wireframes and processes shown in the attached presentation – although intended as a guide only these features and processes all need to be incorporated into the HomePage.
• • Make full use of high quality images and video to convey our brand proposition and products
• Colours as per Logo not as shown below
Nice to have
• • Work in the UK, US/Canada and Australia/NZ and ultimately in mainland Europe.
Should not have
• Must not be cheap or mass-market, nor excessively "stuffy or luxury-orientated"

```html
<!DOCTYPE html>
<html lang="en">
<head>
<meta charset="utf-8">
<title>Bright Journeys – Home</title>
<link href="https://fonts.googleapis.com/css2?family=Lato:wght@300;400;700&family=Bree+Serif&display=swap" rel="stylesheet">
<style>
  :root {
    --navy: #262f6e;
    --forest: #1c5631;
    --lime: #f0f300;
    --ink: #1d1d1d;
    --muted: #444;
    --tile: #e4e4e4;
    --band: #e9e9e9;
    --white: #ffffff;
  }
  * { box-sizing: border-box; margin: 0; padding: 0; }
  html, body { width: 1200px; height: 1000px; overflow: hidden; }
  body { position: relative; font-family: "Lato", sans-serif; color: var(--ink); background: var(--white); }
  .abs { position: absolute; }

  /* header */
  .site-header { position: absolute; left: 0; top: 0; width: 1200px; height: 103px; background: var(--white); }
  .contact-mail { left: 103px; top: 17px; font-size: 12px; display: flex; align-items: center; gap: 5px; }
  .contact-prompt { left: 104px; top: 36px; font-size: 17px; color: var(--muted); font-weight: 400; }
  .contact-phone { left: 103px; top: 64px; font-size: 18px; display: flex; align-items: center; gap: 7px; }
  .brand { left: 500px; top: 22px; width: 196px; text-align: center; }
  .brand-mark { width: 46px; height: 46px; border-radius: 50%; background: var(--forest); margin: 0 auto 6px; }
  .brand-name { font-size: 13px; font-weight: 700; color: var(--forest); letter-spacing: .3px; }
  .utility-links { left: 841px; top: 14px; font-size: 11px; display: flex; gap: 8px; color: var(--ink); }
  .utility-links span.sep { color: var(--muted); }
  .language-flag { left: 1067px; top: 17px; width: 27px; height: 21px; background: linear-gradient(135deg,#1d3b8c,#c8102e 50%,#1d3b8c); }
  .social-row { left: 922px; top: 52px; display: flex; gap: 9px; }
  .social-tile { width: 36px; height: 36px; background: var(--tile); }

  /* navigation */
  .main-nav { position: absolute; left: 0; top: 103px; width: 1200px; height: 58px; background: var(--navy); }
  .nav-item { position: absolute; top: 0; height: 58px; line-height: 60px; font-size: 13.5px; color: var(--white); text-transform: uppercase; white-space: nowrap; }
  .nav-item.is-active { background: var(--forest); width: 57px; text-align: center; }
  .nav-item.is-active::after { content: ""; position: absolute; left: 50%; bottom: -7px; margin-left: -7px; border: 7px solid transparent; border-bottom: 0; border-top-color: var(--forest); }
  .nav-search { display: flex; align-items: center; gap: 7px; }

  /* hero */
  .hero { position: absolute; left: 0; top: 161px; width: 1200px; height: 433px;
    background:
      linear-gradient(180deg, rgba(0,0,0,0) 55%, rgba(60,110,90,.25) 100%),
      linear-gradient(90deg, rgba(0,0,0,0) 55%, #2f7a2c 72%, #3f8f2a 100%),
      linear-gradient(180deg, #3a6fa8 0%, #8ab9de 32%, #d9e9f2 52%, #5aa3c4 62%, #9ccde0 80%, #6f9fb0 100%); }
  .hero-title { left: 344px; top: 215px; width: 509px; height: 163px; background: var(--forest); color: var(--white);
    font-family: "Bree Serif", serif; font-size: 36px; line-height: 55px; text-align: center; padding-top: 27px; letter-spacing: .5px; font-weight: 400; }
  .trip-finder { left: 103px; top: 438px; width: 990px; height: 54px; background: rgba(30,30,30,.75); }
  .finder-select { position: absolute; top: 10px; height: 35px; background: var(--white); font-size: 12.5px; color: var(--ink);
    padding-left: 10px; line-height: 36px; white-space: nowrap; }
  .finder-select svg { position: absolute; right: 10px; top: 13px; }
  .finder-submit { position: absolute; left: 812px; top: 10px; width: 166px; height: 35px; background: var(--lime);
    font-size: 14px; font-weight: 700; text-align: center; line-height: 36px; color: var(--ink); }

  /* about */
  .about-title { left: 0; top: 632px; width: 1200px; text-align: center; font-size: 23px; font-weight: 300; }
  .about-title b { font-weight: 400; }
  .about-copy { left: 0; top: 677px; width: 1200px; text-align: center; font-size: 16px; line-height: 23px; color: var(--ink); }
  .about-copy b { font-weight: 700; }
  .btn-more { left: 531px; top: 741px; width: 129px; height: 39px; background: var(--navy); color: var(--white);
    font-size: 14px; font-weight: 700; text-align: center; line-height: 40px; }

  /* experiences */
  .experiences { position: absolute; left: 0; top: 820px; width: 1200px; height: 180px; background: var(--band); }
  .experiences-title { left: 0; top: 857px; width: 1200px; text-align: center; font-size: 22px; font-weight: 300; }
  .experiences-title b { font-weight: 400; }
  .experience-card { top: 922px; width: 227px; height: 78px; }
</style>
</head>
<body>

<header class="site-header">
  <div class="abs contact-mail">
    <svg width="12" height="10" viewBox="0 0 12 10"><rect x=".5" y=".5" width="11" height="9" fill="none" stroke="#1d1d1d"/><path d="M.5 .8 6 5.5 11.5 .8" fill="none" stroke="#1d1d1d"/></svg>
    support@brightjourneys-demo.com
  </div>
  <div class="abs contact-prompt">For any help or Inquiry ?</div>
  <div class="abs contact-phone">
    <svg width="14" height="14" viewBox="0 0 24 24"><path fill="#1d1d1d" d="M6.6 10.8a15.1 15.1 0 0 0 6.6 6.6l2.2-2.2c.3-.3.7-.4 1-.2 1.1.4 2.3.6 3.6.6.6 0 1 .4 1 1V20c0 .6-.4 1-1 1A17 17 0 0 1 3 4c0-.6.4-1 1-1h3.5c.6 0 1 .4 1 1 0 1.3.2 2.5.6 3.6.1.3 0 .7-.2 1z"/></svg>
    +44 80090017
  </div>

  <div class="abs brand">
    <div class="brand-mark"></div>
    <div class="brand-name">BRIGHT JOURNEYS</div>
  </div>

  <nav class="abs utility-links">
    <span>Privacy &amp; Cookies</span><span class="sep">|</span>
    <span>Terms of Use</span><span class="sep">|</span>
    <span>FAQs</span>
  </nav>
  <div class="abs language-flag" role="img" aria-label="UK flag language selector"></div>
  <div class="abs social-row">
    <div class="social-tile"></div><div class="social-tile"></div><div class="social-tile"></div><div class="social-tile"></div>
  </div>
</header>

<nav class="main-nav">
  <span class="nav-item is-active" style="left:103px">Home</span>
  <span class="nav-item" style="left:174px">Destinations</span>
  <span class="nav-item" style="left:289px">Experiences</span>
  <span class="nav-item" style="left:396px">Trips by Month</span>
  <span class="nav-item" style="left:526px">Topical Now</span>
  <span class="nav-item" style="left:638px">Tailored</span>
  <span class="nav-item" style="left:722px">Pioneers Club</span>
  <span class="nav-item" style="left:844px">Clients Login</span>
  <span class="nav-item" style="left:961px">Blog</span>
  <span class="nav-item nav-search" style="left:1021px">
    <svg width="15" height="15" viewBox="0 0 16 16"><circle cx="6.5" cy="6.5" r="4.8" fill="none" stroke="#fff" stroke-width="2.2"/><path d="M10 10l4.5 4.5" stroke="#fff" stroke-width="2.6" stroke-linecap="round"/></svg>
    Search
  </span>
</nav>

<section class="hero" role="img" aria-label="Tropical backwater lagoon with thatched houseboats, palm trees and blue sky reflected in calm water"></section>
<h1 class="abs hero-title">BRIGHT JOURNEYS<br>IN LESS THAN 7 DAYS !</h1>
<form class="abs trip-finder">
  <div class="finder-select" style="left:9px;width:259px;padding-left:12px">WHAT WOULD YOU LIKE TO DO ?
    <svg width="8" height="9" viewBox="0 0 8 9"><path d="M1 1l3 3 3-3M1 5l3 3 3-3" fill="none" stroke="#333" stroke-width="1.4"/></svg></div>
  <div class="finder-select" style="left:277px;width:259px">WHERE WOULD YOU LIKE TO GO ?
    <svg width="8" height="9" viewBox="0 0 8 9"><path d="M1 1l3 3 3-3M1 5l3 3 3-3" fill="none" stroke="#333" stroke-width="1.4"/></svg></div>
  <div class="finder-select" style="left:545px;width:259px;padding-left:9px">WHENE DO YOU WANT TO TRAVEL ?
    <svg width="8" height="9" viewBox="0 0 8 9"><path d="M1 1l3 3 3-3M1 5l3 3 3-3" fill="none" stroke="#333" stroke-width="1.4"/></svg></div>
  <div class="finder-submit">TAKE ME THERE</div>
</form>

<h2 class="abs about-title">WHO <b>WE ARE</b></h2>
<p class="abs about-copy">Bright Journeys is an online marketplace offering a comprehensive range of '<b>Bucket List</b>'<br>once-in-a-lifetime experiences &amp; events specifically designed for busy working people.</p>
<div class="abs btn-more">READ MORE</div>

<section class="experiences"></section>
<h2 class="abs experiences-title"><b>BRIGHT JOURNEYS</b> In less than 7 Days !</h2>
<div class="abs experience-card" style="left:103px;background:linear-gradient(180deg,#4f6a2e,#6b5b45)" role="img" aria-label="Elephant in the wild"></div>
<div class="abs experience-card" style="left:358px;background:linear-gradient(135deg,#d96a8a,#f0a040 55%,#c94a70)" role="img" aria-label="Crowd at a colour festival"></div>
<div class="abs experience-card" style="left:612px;background:linear-gradient(180deg,#c8c8c8,#6e7479)" role="img" aria-label="Skater on an outdoor court"></div>
<div class="abs experience-card" style="left:866px;background:linear-gradient(135deg,#3d6e57,#8a9a48 50%,#b0426a)" role="img" aria-label="Colourful balloons at a party"></div>

</body>
</html>
```